Website Design for Employee Moral and Happiness Company

Looking for a clean website design that explains our features in a step by step manner so our visitors know exactly what our site does before logging in.

The site is called "Velquo". See logo design and video for a sample of style and an overview of what we do.

Target Market(s)

Business owners that are looking to retain employees.

Number of Pages Required

1 page

```html
<!DOCTYPE html>
<html lang="en">
<head>
<meta charset="utf-8">
<title>Velquo — Employee Morale Events</title>
<link rel="stylesheet" href="https://fonts.googleapis.com/css2?family=Crimson+Pro:wght@400;500&family=Montserrat:wght@400;500;600&display=swap">
<style>
:root{
  --ink:#000000;
  --text:#1a1a1a;
  --muted:#555555;
  --paper:#ffffff;
  --mist:#f3f3f3;
  --soft:#f7f7f7;
  --orange:#ff6600;
  --serif:"Crimson Pro", Georgia, serif;
  --sans:"Montserrat", Arial, sans-serif;
}
*{margin:0;padding:0;box-sizing:border-box}
html,body{width:1200px;height:3746px;overflow:hidden}
body{position:relative;background:var(--paper);font-family:var(--sans);color:var(--text)}
.abs{position:absolute}
.logo{font-family:var(--serif);font-weight:500;font-size:40px;color:var(--ink);letter-spacing:1px;display:flex;align-items:center;gap:8px}
.logo .dot{width:10px;height:10px;border-radius:50%;background:var(--orange)}

.site-header{left:0;top:0;width:1200px;height:94px;background:var(--soft);border-bottom:1px solid #e8e8e8}
.site-header .logo{left:161px;top:22px}
.nav{left:0;top:0;width:1200px;height:94px}
.nav a{position:absolute;top:39px;font-size:12px;line-height:16px;color:var(--text);text-decoration:none;font-weight:500;white-space:nowrap}
.nav .home{left:589px}
.nav .about{left:665px}
.nav .what{left:741px}
.nav .faqs{left:849px}
.btn-outline{left:921px;top:26px;width:116px;height:42px;border:2px solid var(--orange);border-radius:21px;color:var(--orange);font-size:12px;font-weight:600;display:flex;align-items:center;justify-content:center}

.hero{left:0;top:94px;width:1200px;height:732px;background:#f6f6f6}
.eyebrow{left:161px;top:211px;font-size:12px;letter-spacing:2.4px;color:var(--orange);font-weight:500}
.hero-title{left:161px;top:236px;font-family:var(--serif);font-weight:500;font-size:44px;line-height:56px;color:var(--ink);white-space:nowrap}
.underline{left:300px;top:346px}
.btn-solid{background:var(--orange);color:#fff;font-size:12px;font-weight:600;border-radius:21px;display:flex;align-items:center;justify-content:center}
.hero .cta{left:161px;top:400px;width:118px;height:42px}
.play{left:293px;top:400px;width:42px;height:42px;border-radius:50%;background:var(--ink);display:flex;align-items:center;justify-content:center}
.art{border-radius:6px}
.hero-art{left:676px;top:67px;width:461px;height:494px;background:linear-gradient(160deg,#eeeeee 0%,#f4f4f4 50%,#e9e9e9 100%)}

.card{background:#fff;box-shadow:0 4px 18px rgba(0,0,0,.08)}
.board-card{left:161px;top:768px;width:358px;height:392px}
.board-card .art{position:absolute;left:16px;top:14px;width:326px;height:305px;background:linear-gradient(180deg,#ececec,#f2f2f2)}
.pin{width:10px;height:10px;border-radius:50%;background:var(--orange)}
.section-title{font-family:var(--serif);font-weight:500;color:var(--ink)}
.retention{left:576px;top:932px;font-size:34px;line-height:45px;white-space:nowrap}
.link-more{left:576px;top:1055px;font-size:11px;font-weight:600;color:var(--orange);display:flex;align-items:center;gap:6px}

.planner-title{left:0;top:1265px;width:1200px;text-align:center;font-size:36px}
.planner-copy{left:300px;top:1322px;width:600px;text-align:center;font-size:12px;line-height:24px;color:var(--muted)}
.planner-art{left:161px;top:1377px;width:876px;height:437px;background:linear-gradient(180deg,#f1f1f1 0%,#e6e1d6 55%,#ebebeb 100%)}
.accent-bar{left:1080px;top:1359px;width:120px;height:367px;background:var(--orange)}

.transform-band{left:0;top:1923px;width:1037px;height:602px;background:#f5f5f5}
.transform-title{left:161px;top:2118px;font-size:36px;line-height:46px}
.transform-copy{left:161px;top:2234px;width:360px;font-size:11.5px;line-height:24px;color:var(--text)}
.mood-card{top:2036px;width:277px;height:374px}
.mood-card .art{position:absolute;left:13px;top:14px;width:251px;height:284px;background:linear-gradient(180deg,#e7e7e7,#efefef)}
.mood-card .label{position:absolute;left:0;width:100%;top:330px;text-align:center;font-size:13px;color:var(--orange)}
.mood-card .pin{position:absolute;left:131px;top:-12px}
.from{left:594px}
.to{left:894px}

.step{top:2640px;display:flex;gap:26px;align-items:flex-start}
.step .num{font-family:var(--serif);font-weight:400;font-size:96px;line-height:84px;color:transparent;-webkit-text-stroke:1.3px var(--orange)}
.step p{width:230px;font-size:11.5px;line-height:24px;padding-top:2px}
.step-1{left:161px}
.step-2{left:683px}

.question{left:161px;top:2966px;font-size:34px}
.question-art{left:505px;top:2860px;width:290px;height:290px;border-radius:50%;background:radial-gradient(circle at 50% 50%,#d4d4d4 0%,#dedede 100%)}
.question-cta{left:921px;top:2972px;width:116px;height:42px}

.site-footer{left:0;top:3162px;width:1200px;height:584px;background:linear-gradient(180deg,#f3f3f3,#f8f8f8)}
.site-footer .logo{left:161px;top:115px}
.socials{left:161px;top:176px;display:flex;gap:12px}
.socials span{width:11px;height:11px;border-radius:50%;background:var(--orange)}
.col{top:112px}
.col h4{font-family:var(--serif);font-weight:500;font-size:17px;color:var(--ink);margin-bottom:12px}
.col li{list-style:none;font-size:10.5px;line-height:26px;color:var(--text)}
.col-links{left:461px}
.col-res{left:681px}
.col-touch{left:912px}
.col-touch li{display:flex;align-items:center;gap:8px}
</style>
</head>
<body>

<header class="abs site-header">
  <div class="abs logo">Velquo<span class="dot"></span></div>
  <nav class="abs nav">
    <a class="home">Home</a>
    <a class="about">About</a>
    <a class="what">What We Do</a>
    <a class="faqs">FAQs</a>
  </nav>
  <div class="abs btn-outline">Contact Us</div>
</header>

<section class="abs hero">
  <div class="abs eyebrow">WELCOME TO VELQUO</div>
  <h1 class="abs hero-title">Do Your Employess<br>Need a Morale Boost?</h1>
  <svg class="abs underline" width="130" height="8" viewBox="0 0 130 8"><path d="M2 6 Q65 0 128 4" fill="none" stroke="#ff6600" stroke-width="1.4"/></svg>
  <div class="abs btn-solid cta">Get Started</div>
  <div class="abs play"><svg width="14" height="16" viewBox="0 0 14 16"><path d="M2 1 L13 8 L2 15 Z" fill="#ff6600"/></svg></div>
  <div class="abs art hero-art" role="img" aria-label="Illustration of an employee working at a desk with a laptop, a clock, sticky notes and a work progress bar at 45%"></div>
</section>

<section>
  <div class="abs card board-card">
    <div class="art" role="img" aria-label="Illustration of two colleagues arranging tasks on a to do, work and done board"></div>
  </div>
  <div class="abs pin" style="left:335px;top:760px"></div>
  <h2 class="abs section-title retention">Start building your event,<br>increase employee’s retention!</h2>
  <div class="abs link-more">Explore More
    <svg width="16" height="8" viewBox="0 0 16 8"><path d="M0 4 H14 M10 1 L14 4 L10 7" fill="none" stroke="#ff6600" stroke-width="1.3"/></svg>
  </div>
</section>

<section>
  <h2 class="abs section-title planner-title">All-in-One Event Planner</h2>
  <p class="abs planner-copy">Lorem ipsum dolor sit amet, consectetur adipiscing elit, sed do eiusmod tempor incididunt ut labore et dolore magna aliqua. Quis ipsum suspendisse ultrices gravida.</p>
  <div class="abs art planner-art" role="img" aria-label="Illustration of a person sitting beside a large laptop showing an event planner dashboard with schedule, messages and tasks"></div>
  <div class="abs accent-bar"></div>
</section>

<section>
  <div class="abs transform-band"></div>
  <h2 class="abs section-title transform-title">Transform Your<br>Work Events</h2>
  <p class="abs transform-copy">Lorem ipsum dolor sit amet, consectetur adipiscing elit, sed do eiusmod tempor incididunt ut labore et dolore magna aliqua. Quis ipsum suspendisse ultrices gravida. Risus commodo viverra maecenas accumsan lacus vel facilisis.</p>
  <div class="abs card mood-card from">
    <div class="pin"></div>
    <div class="art" role="img" aria-label="Illustration of a stressed employee holding their head at a desk"></div>
    <div class="label">From This</div>
  </div>
  <div class="abs card mood-card to">
    <div class="pin"></div>
    <div class="art" role="img" aria-label="Illustration of a happy employee jumping with joy"></div>
    <div class="label">To This</div>
  </div>
</section>

<section>
  <div class="abs step step-1">
    <div class="num">01</div>
    <p>Lorem ipsum dolor sit amet, consectetur adipiscing elit, sed do eiusmod tempor didunt ut labore et dolore magna aliqua.</p>
  </div>
  <div class="abs step step-2">
    <div class="num">02</div>
    <p>Lorem ipsum dolor sit amet, consectetur adipiscing elit, sed do eiusmod tempor didunt ut labore et dolore magna aliqua.</p>
  </div>
</section>

<section>
  <h2 class="abs section-title question">Any Question?</h2>
  <div class="abs question-art" role="img" aria-label="Illustration of a thoughtful woman with a question thought bubble beside a plant"></div>
  <div class="abs btn-solid question-cta">Contact Us</div>
</section>

<footer class="abs site-footer">
  <div class="abs logo">Velquo<span class="dot"></span></div>
  <div class="abs socials"><span></span><span></span><span></span><span></span></div>
  <div class="abs col col-links">
    <h4>Links</h4>
    <ul><li>Home</li><li>What We Do</li><li>FAQs</li><li>Contact</li></ul>
  </div>
  <div class="abs col col-res">
    <h4>Resources</h4>
    <ul><li>Lorem Ipsum</li><li>Dolor Amet</li><li>Lorem Ipsum</li><li>Dolor Amet</li></ul>
  </div>
  <div class="abs col col-touch">
    <h4>Get in Touch</h4>
    <ul>
      <li><svg width="11" height="8" viewBox="0 0 11 8"><rect x="0.5" y="0.5" width="10" height="7" fill="#ff6600"/><path d="M0.5 0.5 L5.5 4.5 L10.5 0.5" fill="none" stroke="#fff" stroke-width="1"/></svg>email@example.com</li>
      <li><svg width="10" height="10" viewBox="0 0 10 10"><path d="M2 0.5 L3.8 0.5 L4.5 3 L3.2 4 Q4.3 6 6 6.8 L7 5.5 L9.5 6.2 L9.5 8 Q9.5 9.5 8 9.5 Q1 9 0.5 2 Q0.5 0.5 2 0.5 Z" fill="#ff6600"/></svg>+1 234 567 890</li>
    </ul>
  </div>
</footer>

</body>
</html>
```